Meridian Handsets business card design

I would like to see some designs for a business card for Meridian Handsets. I would like the business card to be double sided. It will need to have a similar colour / look and feel to our website www.meridianhandsets.com.au I have also attached our latest flyer. Final designs to be handed over in Photoshop format so that I can edit the business card when needed please.

Industry/Entity Type

Business

Contact Information for Business Card

Gavin Thornley
sales@meridianhandsets.com.au
Business Development Manager
ph: (08) 6197 5821
www.meridianhandsets.com.au

Font styles to use
Serif
Sans Serif

Requirements
Must have
• If you could please utilise our colour scheme as seen on our website and the attached flyer.
• I would also like the final design to be in a Photoshop format so that I can edit it when needed please.

```html
<!DOCTYPE html>
<html lang="en">
<head>
<meta charset="utf-8">
<title>Meridian Handsets – Business Card</title>
<link rel="stylesheet" href="https://fonts.googleapis.com/css2?family=Arimo:wght@400;700&display=swap">
<style>
  :root {
    --page-bg: #2a2a2a;
    --card-bg: #efefef;
    --ink: #333333;
    --ink-soft: #1e1e1e;
    --brand-blue: #0a76b5;
    --card-shadow: 0 4px 10px rgba(0,0,0,0.45);
  }
  * { box-sizing: border-box; margin: 0; padding: 0; }
  html, body {
    width: 1200px;
    height: 800px;
    overflow: hidden;
    background: var(--page-bg);
    font-family: "Arimo", Arial, sans-serif;
  }
  .card-set {
    position: absolute;
    left: 44px;
    top: 246px;
    display: flex;
    gap: 32px;
  }
  .card {
    position: relative;
    width: 540px;
    height: 308px;
    background: var(--card-bg);
    box-shadow: var(--card-shadow);
    overflow: hidden;
  }
  .wordmark {
    font-family: "Arimo", Arial, sans-serif;
    font-weight: 700;
    color: var(--ink);
    letter-spacing: -0.5px;
    white-space: nowrap;
  }
  .card-front .wordmark {
    position: absolute;
    left: 40px;
    top: 52px;
    font-size: 42px;
  }
  .person {
    position: absolute;
    left: 39px;
    top: 140px;
  }
  .person-name {
    font-size: 21px;
    color: var(--brand-blue);
    font-weight: 400;
    line-height: 1.1;
  }
  .person-title {
    font-size: 14px;
    color: var(--ink-soft);
    margin-top: 2px;
  }
  .contact-list {
    position: absolute;
    left: 39px;
    top: 214px;
    list-style: none;
  }
  .contact-item {
    display: flex;
    align-items: center;
    gap: 8px;
    font-size: 14px;
    color: var(--ink-soft);
    height: 21.5px;
  }
  .contact-icon { width: 11px; height: 11px; flex: none; }
  .card-back {
    display: flex;
    align-items: center;
    justify-content: center;
  }
  .card-back .wordmark {
    font-size: 48px;
    margin-top: -6px;
  }
</style>
</head>
<body>
  <main class="card-set">
    <section class="card card-front" aria-label="Business card front">
      <div class="wordmark">Meridian Handsets</div>
      <div class="person">
        <h1 class="person-name">Gavin Thornley</h1>
        <p class="person-title">Business Development Manager</p>
      </div>
      <ul class="contact-list">
        <li class="contact-item">
          <svg class="contact-icon" viewBox="0 0 12 12" aria-hidden="true">
            <rect width="12" height="12" fill="var(--brand-blue)"/>
            <path d="M4 2.5 L5.3 4.2 L4.6 5 Q5.5 7 7 7.4 L7.8 6.7 L9.5 8 L8.6 9.5 Q5 9.5 2.6 4 Z" fill="#fff"/>
          </svg>
          (08) 6197 5821
        </li>
        <li class="contact-item">
          <svg class="contact-icon" viewBox="0 0 12 12" aria-hidden="true">
            <rect width="12" height="12" fill="var(--brand-blue)"/>
            <circle cx="6" cy="6" r="3.6" fill="none" stroke="#fff" stroke-width="1"/>
            <path d="M2.4 6 H9.6 M6 2.4 Q4 6 6 9.6 M6 2.4 Q8 6 6 9.6" fill="none" stroke="#fff" stroke-width="0.8"/>
          </svg>
          www.meridianhandsets.com.au
        </li>
        <li class="contact-item">
          <svg class="contact-icon" viewBox="0 0 12 12" aria-hidden="true">
            <rect width="12" height="12" fill="var(--brand-blue)"/>
            <rect x="2.5" y="3.5" width="7" height="5" fill="#fff"/>
            <path d="M2.5 3.5 L6 6.5 L9.5 3.5" fill="none" stroke="var(--brand-blue)" stroke-width="0.8"/>
          </svg>
          sales@meridianhandsets.com.au
        </li>
      </ul>
    </section>
    <section class="card card-back" aria-label="Business card back">
      <div class="wordmark">Meridian Handsets</div>
    </section>
  </main>
</body>
</html>
```